Marlow Creek sign

24"x36" sign for new home construction job site. Located in affluent in-town neighborhood in Midwest. Traditional american style homes. 2nd generation construction company. Sign needs to convey strength and elegance but not overly elaborate. Competition most has signs consisting of text.

Sign text reads:
Marlow Creek Builders
Custom Luxury for Over 20 years
248-555-0137

Target Market(s)

Upper middle income home buyers

Industry/Entity Type

Construction

Font styles to use
Serif
Decorative

Requirements
Must have
• Logo image no more than 2 colors
Nice to have
• Should be visible and legible from distance of 30'
Should not have
• Not just image of house as logo

```html
<!DOCTYPE html>
<html lang="en">
<head>
<meta charset="utf-8">
<title>Marlow Creek Builders – Job Site Sign</title>
<link rel="stylesheet" href="https://fonts.googleapis.com/css2?family=Montserrat:wght@600&family=Ubuntu:wght@400;500&display=swap">
<style>
  :root {
    --orange: #f38a35;
    --charcoal: #3a3839;
    --grey: #9d9d9d;
    --rule: #6f6f6f;
    --paper: #ffffff;
  }
  html, body {
    margin: 0;
    padding: 0;
    overflow: hidden;
    background: var(--paper);
  }
  .sign {
    position: relative;
    width: 1200px;
    height: 800px;
    overflow: hidden;
    background: var(--paper);
  }
  .sign-art {
    position: absolute;
    inset: 0;
  }
  .brand-mark {
    position: absolute;
    left: 538px;
    top: 70px;
    width: 124px;
    height: 124px;
    background: var(--orange);
    transform: rotate(45deg);
  }
  .brand-name {
    position: absolute;
    left: 0;
    width: 1200px;
    margin: 0;
    text-align: center;
    font-family: "Montserrat", sans-serif;
    font-weight: 600;
    color: var(--charcoal);
  }
  .brand-name__primary {
    top: 262px;
    font-size: 96px;
    line-height: 1;
    letter-spacing: -1px;
  }
  .brand-rule {
    position: absolute;
    left: 205px;
    top: 367px;
    width: 792px;
    height: 1px;
    background: var(--rule);
  }
  .brand-name__secondary {
    top: 388px;
    font-size: 54px;
    line-height: 1;
    letter-spacing: 55px;
    text-indent: 55px;
  }
  .tagline {
    position: absolute;
    left: 0;
    width: 1200px;
    top: 560px;
    margin: 0;
    text-align: center;
    font-family: "Ubuntu", sans-serif;
    font-weight: 400;
    font-size: 53px;
    line-height: 1;
    color: var(--charcoal);
  }
  .phone {
    position: absolute;
    left: 120px;
    top: 640px;
    display: flex;
    align-items: center;
    gap: 72px;
  }
  .phone__icon {
    width: 40px;
    height: 78px;
  }
  .phone__number {
    font-family: "Ubuntu", sans-serif;
    font-weight: 500;
    font-size: 126px;
    line-height: 1;
    color: var(--charcoal);
  }
</style>
</head>
<body>
  <main class="sign">
    <svg class="sign-art" width="1200" height="800" viewBox="0 0 1200 800" aria-hidden="true">
      <defs>
        <clipPath id="wave-clip">
          <path d="M0 540 C 300 500, 700 470, 1000 472 C 1110 474, 1170 500, 1200 515 L1200 800 L0 800 Z"/>
        </clipPath>
      </defs>
      <path class="wave-swoosh" d="M0 505 C 300 520, 700 470, 1070 482 C 900 472, 500 510, 0 530 Z" fill="var(--grey)"/>
      <path class="wave-band" d="M0 540 C 300 500, 700 470, 1000 472 C 1110 474, 1170 500, 1200 515 L1200 800 L0 800 Z" fill="var(--orange)"/>
      <rect class="frame" x="13" y="13" width="1174" height="774" fill="none" stroke="var(--orange)" stroke-width="2"/>
      <rect class="frame frame--light" x="13" y="13" width="1174" height="774" fill="none" stroke="var(--paper)" stroke-width="2" clip-path="url(#wave-clip)"/>
    </svg>

    <div class="brand-mark" aria-hidden="true"></div>
    <h1 class="brand-name brand-name__primary">MARLOW CREEK</h1>
    <div class="brand-rule" aria-hidden="true"></div>
    <p class="brand-name brand-name__secondary">BUILDERS</p>

    <p class="tagline">Custom Luxury for Over 20 years</p>

    <div class="phone">
      <svg class="phone__icon" viewBox="0 0 40 78" aria-hidden="true">
        <path d="M3 3 H27 L37 13 V75 H3 Z" fill="none" stroke="var(--charcoal)" stroke-width="4" stroke-linejoin="round"/>
        <rect x="11" y="25" width="18" height="20" fill="none" stroke="var(--charcoal)" stroke-width="4"/>
      </svg>
      <span class="phone__number">248-555-0137</span>
    </div>
  </main>
</body>
</html>
```